Business Card for Business consulting practice

Need a design for a consultant business card. Simple and elegant.
I need the following information on the card:
Logo: (see uploaded file)
Company name: Callendry Advisory Group
Name: Noel Fardwick
Title: Managing Director - Aerospace and Defence
Phone #: 438-261-7083
e-mail: noel.fardwick@callendry.example
Website: www.callendry.example
Tagline: Proposals Management and Capture support for complex procurements

```html
<!DOCTYPE html>
<html lang="en">
<head>
<meta charset="utf-8">
<title>Callendry Advisory Group — Business Card</title>
<link href="https://fonts.googleapis.com/css2?family=Raleway:wght@400;500;700&display=swap" rel="stylesheet">
<style>
  :root {
    --navy: #0f2f45;
    --ink: #12283a;
    --accent: #1a8dc0;
    --paper: #ffffff;
    --backdrop: #e9ecef;
    --body-text: #1b1b1b;
  }
  * { margin: 0; padding: 0; box-sizing: border-box; }
  html, body { width: 1200px; height: 900px; overflow: hidden; }
  body {
    background: var(--backdrop);
    font-family: "Raleway", sans-serif;
    position: relative;
  }
  .card {
    position: absolute;
    left: 250px;
    width: 700px;
    height: 400px;
    border-radius: 22px;
    overflow: hidden;
    box-shadow: 0 6px 18px rgba(0,0,0,0.18);
  }
  .card--front { top: 30px; background: var(--navy); }
  .card--back { top: 470px; background: var(--paper); }

  .brand {
    position: absolute;
    left: 0; right: 0;
    display: flex;
    justify-content: center;
  }
  .brand__name {
    display: flex;
    align-items: center;
    gap: 12px;
    font-weight: 500;
    font-size: 36px;
    letter-spacing: 2px;
    line-height: 1;
    white-space: nowrap;
  }
  .brand__dot {
    width: 22px; height: 22px;
    border-radius: 50%;
    background: var(--accent);
    flex: none;
  }
  .brand__rule {
    position: absolute;
    height: 2px;
    background: var(--accent);
  }
  .card--front .brand { top: 168px; }
  .card--front .brand__name { color: var(--paper); }
  .card--front .brand__rule { top: 226px; left: 90px; right: 90px; }

  .card--back .brand { top: 165px; }
  .card--back .brand__name { color: var(--ink); }
  .card--back .brand__rule { top: 222px; left: 0; right: 0; }

  .person {
    position: absolute;
    top: 36px; left: 0; right: 0;
    text-align: center;
  }
  .person__name {
    color: var(--accent);
    font-weight: 700;
    font-size: 28px;
    letter-spacing: 0.5px;
  }
  .person__role {
    color: var(--body-text);
    font-size: 19px;
    line-height: 1.25;
    margin-top: 2px;
  }
  .contact {
    position: absolute;
    top: 244px; left: 0; right: 0;
    text-align: center;
    color: var(--body-text);
    font-size: 20px;
    line-height: 1.22;
  }
  .tagline {
    position: absolute;
    bottom: 24px; left: 0; right: 0;
    text-align: center;
    color: var(--accent);
    font-size: 18px;
    font-weight: 500;
    white-space: nowrap;
  }
</style>
</head>
<body>
  <section class="card card--front" aria-label="Card front">
    <div class="brand">
      <div class="brand__name"><span class="brand__dot"></span>Callendry Advisory Group</div>
    </div>
    <div class="brand__rule"></div>
  </section>

  <section class="card card--back" aria-label="Card back">
    <div class="person">
      <div class="person__name">NOEL FARDWICK</div>
      <div class="person__role">Managing Director<br>Aerospace and Defence</div>
    </div>
    <div class="brand">
      <div class="brand__name"><span class="brand__dot"></span>Callendry Advisory Group</div>
    </div>
    <div class="brand__rule"></div>
    <div class="contact">
      <div>438-261-7083</div>
      <div>noel.fardwick@callendry.example</div>
      <div>www.callendry.example</div>
    </div>
    <div class="tagline">Proposals Management and Capture support for complex procurements</div>
  </section>
</body>
</html>
```